Business card, letterhead, envelope design, email footer for non-profit private equity association
Riviera Growth Capital and Seed Funding Society
Business card, letterhead, envelope design, email footer for non-profit private equity association - Financial Services
Creative Brief
Simple
Tobias Hernquist
Head of Operations
17, Rue des Orangers 98000 Monaco
thernquist@rgsf-example.org
www.rgsf-example.org
Stationery will be prepared for all 7-8 Board Members of our non-profit association. The stationery design is a subsequent process of the new logo design, which has just been created. The Riviera Growth Capital & Seed Funding Society (RGSF) stands for: seriousness and professionalism. Our official website is http://www.rgsf-example.org Please note that this website still includes the OLD logo and layout (to be changed shortly, so please do not let that influence you. This is more to show you the content rather than the design.

```html
<!DOCTYPE html>
<html lang="en">
<head>
<meta charset="utf-8">
<title>RGSF Business Card</title>
<link href="https://fonts.googleapis.com/css2?family=Montserrat:wght@400;500;700&display=swap" rel="stylesheet">
<style>
  :root {
    --bg: #e9e6e1;
    --paper: #ffffff;
    --ink: #2e2e30;
    --band: #3b3b3d;
    --accent: #d9262b;
    --muted: #d8d8d8;
  }
  * { margin: 0; padding: 0; box-sizing: border-box; }
  html, body { width: 1200px; height: 899px; overflow: hidden; }
  body {
    background: var(--bg);
    font-family: "Montserrat", Arial, sans-serif;
    position: relative;
  }
  .card {
    position: absolute;
    width: 540px;
    height: 309px;
    background: var(--paper);
    box-shadow: 0 6px 18px rgba(0,0,0,.18);
    overflow: hidden;
  }
  .card-back { left: 40px; top: 295px; }
  .card-front { left: 620px; top: 295px; }

  .brand { position: absolute; color: var(--ink); font-weight: 700; }
  .brand-name { font-size: 58px; letter-spacing: 2px; line-height: 1; }
  .brand-full { font-size: 11px; line-height: 1.35; letter-spacing: .4px; text-transform: uppercase; margin-top: 6px; width: 250px; }

  .card-front .brand { left: 140px; top: 100px; }
  .card-back .brand { left: 26px; top: 26px; }
  .card-back .brand-name { font-size: 46px; }
  .card-back .brand-full { font-size: 9.5px; width: 220px; }

  .band { position: absolute; inset: 0; }

  .person { position: absolute; right: 40px; top: 108px; text-align: right; }
  .person-name { color: var(--accent); font-size: 15px; font-weight: 500; letter-spacing: 1px; text-transform: uppercase; }
  .person-title { color: var(--ink); font-size: 12px; margin-top: 3px; }

  .contacts { position: absolute; left: 26px; top: 172px; list-style: none; color: var(--muted); font-size: 10.5px; }
  .contacts li { display: flex; align-items: center; gap: 8px; height: 22px; }
  .contacts svg { width: 12px; height: 12px; fill: var(--muted); }

  .address { position: absolute; left: 330px; top: 228px; color: var(--muted); font-size: 11px; line-height: 1.5; }
  .website { position: absolute; left: 330px; top: 276px; color: var(--paper); font-size: 12px; }
</style>
</head>
<body>
  <section class="card card-back">
    <svg class="band" viewBox="0 0 540 309" width="540" height="309" aria-hidden="true">
      <path d="M0,160 C220,166 400,200 540,240 L540,309 L0,309 Z" fill="var(--band)"/>
      <path d="M0,152 C220,158 400,192 540,232" fill="none" stroke="var(--accent)" stroke-width="3"/>
    </svg>
    <div class="brand">
      <div class="brand-name">RGSF</div>
      <div class="brand-full">Riviera Growth Capital and Seed Funding Society</div>
    </div>
    <div class="person">
      <div class="person-name">Tobias Hernquist</div>
      <div class="person-title">Managing Director</div>
    </div>
    <ul class="contacts">
      <li><svg viewBox="0 0 12 12"><path d="M2.5 1h2l1 3-1.3 1a6 6 0 0 0 2.8 2.8L8 6.5l3 1v2c0 .8-.7 1.5-1.5 1.5A8.5 8.5 0 0 1 1 2.5C1 1.7 1.7 1 2.5 1z"/></svg>012 555 0148</li>
      <li><svg viewBox="0 0 12 12"><path d="M3.5 0h5a1 1 0 0 1 1 1v10a1 1 0 0 1-1 1h-5a1 1 0 0 1-1-1V1a1 1 0 0 1 1-1zm.5 1.5v7.5h4V1.5z"/></svg>012 555 0149</li>
      <li><svg viewBox="0 0 12 12"><path d="M3 0h5v3H3zM1 4h10v6H9v2H3v-2H1zm3 4v3h4V8z"/></svg>012 555 0150</li>
      <li><svg viewBox="0 0 12 12"><path d="M0 2h12v8H0zm1 1v.4l5 3.2 5-3.2V3z"/></svg>thernquist@rgsf-example.org</li>
    </ul>
    <div class="address">17, Rue des Orangers<br>98000 Monaco</div>
    <div class="website">www.rgsf-example.org</div>
  </section>

  <section class="card card-front">
    <div class="brand">
      <div class="brand-name">RGSF</div>
      <div class="brand-full">Riviera Growth Capital and Seed Funding Society</div>
    </div>
  </section>
</body>
</html>
```